Brellow Business Card Re-design

Our current cards are outdated. This is our website www.brellowinsight.com. We would like something that is "on-brand" and consistent with our social media sites. We are strategic consultants with a core competency in Marketing Research. Although, please know we are considering a brand logo redesign and potentially a new look. If we like your work here we will invite you to participate when we get to that project. Thank you very much. Corabel
Here are our social sites: https://chirvalo.com/Brellow?lang=en
https://plus.quarnix.com/+Brellowinsight
https://www.workvelt.com/company/4958207/
https://www.friendlumo.com/BrellowInc/
Project Deadline Extended Reason: We appreciate the designs that have been submitted. We are extending the deadline because not everyone in our office has been available until now to view the designs. Thank you. Added Monday, September 25, 2017
Industry/Entity Type
Business
Look and feel

```html
<!DOCTYPE html>
<html lang="en">
<head>
<meta charset="utf-8">
<title>Brellow Business Card</title>
<link rel="stylesheet" href="https://fonts.googleapis.com/css2?family=Arimo:wght@400;700&display=swap">
<style>
  :root {
    --brand-green: #7fa24a;
    --brand-blue: #4a74a6;
    --card-white: #f7f7f5;
    --ink: #1f1f1f;
    --stage: #e8e9ea;
  }
  html, body {
    margin: 0;
    padding: 0;
    width: 1200px;
    height: 1000px;
    overflow: hidden;
    background: var(--stage);
    font-family: "Arimo", Arial, sans-serif;
  }
  .card {
    position: absolute;
    left: 250px;
    width: 700px;
    height: 400px;
    background: var(--card-white);
    overflow: hidden;
    box-shadow: 0 2px 6px rgba(0,0,0,0.12);
  }
  .card-front { top: 50px; }
  .card-back { top: 530px; }
  .card-shapes {
    position: absolute;
    inset: 0;
    width: 700px;
    height: 400px;
  }
  .shape-blue { fill: var(--brand-blue); }
  .shape-green { fill: var(--brand-green); }

  /* front */
  .front-wordmark {
    position: absolute;
    left: 80px;
    top: 115px;
    margin: 0;
    font-weight: 700;
    font-size: 130px;
    line-height: 1;
    letter-spacing: -3px;
    color: var(--brand-green);
    white-space: nowrap;
  }
  .front-wordmark .suffix {
    font-size: 28px;
    letter-spacing: 0;
    vertical-align: top;
    margin-left: 6px;
  }
  .front-url {
    position: absolute;
    left: 86px;
    top: 272px;
    margin: 0;
    font-size: 28px;
    font-weight: 700;
    color: var(--brand-green);
  }

  /* back */
  .back-wordmark {
    position: absolute;
    left: -26px;
    top: 132px;
    width: 360px;
    height: 72px;
    margin: 0;
    text-align: center;
    font-weight: 700;
    font-size: 70px;
    line-height: 72px;
    color: #ffffff;
    white-space: nowrap;
    transform: rotate(-50deg);
    transform-origin: center;
  }
  .back-wordmark .suffix {
    font-size: 17px;
    line-height: 1;
    vertical-align: top;
    margin-left: 3px;
  }
  .holder {
    position: absolute;
    left: 372px;
    top: 128px;
    width: 306px;
  }
  .holder-name {
    margin: 0;
    font-size: 28px;
    font-weight: 700;
    color: var(--brand-green);
    white-space: nowrap;
  }
  .holder-name .surname { color: var(--brand-blue); }
  .holder-rule {
    height: 3px;
    background: var(--brand-green);
    margin: 8px 0 6px;
  }
  .holder-role {
    margin: 0;
    font-size: 22px;
    color: var(--brand-green);
  }
  .contact-list {
    position: absolute;
    left: 374px;
    top: 250px;
    margin: 0;
    padding: 0;
    list-style: none;
  }
  .contact-item {
    display: flex;
    align-items: center;
    height: 40px;
    font-size: 21px;
    color: var(--brand-green);
    white-space: nowrap;
  }
  .contact-icon {
    width: 32px;
    height: 32px;
    margin-right: 14px;
    flex: none;
  }
  .icon-stroke { fill: none; stroke: var(--ink); stroke-width: 2.2; }
  .icon-fill { fill: var(--ink); }
</style>
</head>
<body>

<section class="card card-front" aria-label="Card front">
  <svg class="card-shapes" viewBox="0 0 700 400" aria-hidden="true">
    <polygon class="shape-blue" points="0,0 245,0 0,170"/>
    <polygon class="shape-blue" points="700,40 700,400 470,400"/>
  </svg>
  <p class="front-wordmark">brellow<span class="suffix">inc.</span></p>
  <p class="front-url">www.brellowinsight.com</p>
</section>

<section class="card card-back" aria-label="Card back">
  <svg class="card-shapes" viewBox="0 0 700 400" aria-hidden="true">
    <polygon class="shape-green" points="0,0 360,0 25,400 0,400"/>
    <polygon class="shape-blue" points="25,400 210,180 235,400"/>
    <polygon class="shape-blue" points="520,0 700,0 700,105"/>
  </svg>
  <p class="back-wordmark">brellow<span class="suffix">inc</span></p>

  <div class="holder">
    <p class="holder-name">Corabel <span class="surname">Pellingham</span></p>
    <div class="holder-rule"></div>
    <p class="holder-role">Marketing Researcher</p>
  </div>

  <ul class="contact-list">
    <li class="contact-item">
      <svg class="contact-icon" viewBox="0 0 34 34" aria-hidden="true">
        <rect class="icon-stroke" x="9" y="3" width="16" height="28" rx="3"/>
        <rect class="icon-fill" x="12" y="7" width="10" height="18"/>
      </svg>
      +1-555-730-018
    </li>
    <li class="contact-item">
      <svg class="contact-icon" viewBox="0 0 34 34" aria-hidden="true">
        <rect class="icon-fill" x="2" y="8" width="30" height="20"/>
        <polyline points="2,8 17,20 32,8" fill="none" stroke="#f7f7f5" stroke-width="2"/>
      </svg>
      info@brellowinsight.com
    </li>
    <li class="contact-item">
      <svg class="contact-icon" viewBox="0 0 34 34" aria-hidden="true">
        <circle class="icon-stroke" cx="17" cy="17" r="14"/>
        <ellipse class="icon-stroke" cx="17" cy="17" rx="6" ry="14"/>
        <line class="icon-stroke" x1="3" y1="17" x2="31" y2="17"/>
        <line class="icon-stroke" x1="17" y1="3" x2="17" y2="31"/>
        <line class="icon-stroke" x1="6" y1="10" x2="28" y2="10"/>
        <line class="icon-stroke" x1="6" y1="24" x2="28" y2="24"/>
      </svg>
      www.brellowinsight.com
    </li>
  </ul>
</section>

</body>
</html>
```